The name of the company is Kestrel Rehab buying foreclosed homes and remodeling

A sleek classy card. It’s a home remodel and house flip company. Something mostly black with dark gray and red in color . Something with two f”s as a logo on front as shown in pictures. Kind of just let you guys run with it . I left a few pictures that should help
You guys get an idea of what I thought was good also left all the information for back of the card

Target Market(s)

Home remodel consumers

Industry/Entity Type

Construction Company

Contact Information for Business Card

All details are on photo

Font styles to use
Decorative

Colors

Designer to choose colors to be used in the design.

Requirements
Must have
• Name of company on front. Kestrel Rehab
Nice to have
• Up to you guys I trust you
Should not have
• Not sure

```html
<!DOCTYPE html>
<html lang="en">
<head>
<meta charset="utf-8">
<title>Kestrel Rehab – Business Card</title>
<link rel="stylesheet" href="https://fonts.googleapis.com/css2?family=Fira+Sans+Condensed:wght@400;500&family=Libre+Baskerville:ital,wght@1,700&display=swap">
<style>
  :root {
    --page: #ffffff;
    --card: #000000;
    --ink: #f2f2f2;
    --brand: #c07480;
    --accent: #9a4557;
    --label: #cfcfcf;
  }
  * { margin: 0; padding: 0; box-sizing: border-box; }
  html, body {
    width: 927px; height: 1200px; overflow: hidden;
    background: var(--page);
  }
  body { position: relative; font-family: "Fira Sans Condensed", Arial, sans-serif; }

  .card {
    position: absolute;
    background: var(--card);
    color: var(--ink);
  }
  .card--front { left: 288px; top: 339px; width: 380px; height: 216px; }
  .card--back  { left: 288px; top: 642px; width: 377px; height: 218px; }

  .front-wordmark {
    position: absolute; left: 0; right: 0; top: 50%;
    transform: translateY(-50%);
    text-align: center;
    font-size: 26px; font-weight: 500;
    letter-spacing: 1px;
    color: var(--accent);
  }

  .back-brand {
    position: absolute; left: 45px; top: 19px;
    font-size: 15px; color: var(--brand);
  }
  .back-name {
    position: absolute; left: 145px; top: 19px;
    font-size: 15px; color: var(--ink);
  }
  .back-roles {
    position: absolute; left: 45px; top: 46px;
    font-size: 11.5px; color: var(--ink);
    white-space: nowrap;
  }
  .back-roles .role { position: absolute; top: 0; }
  .role--gc { left: 0; }
  .role--remodel { left: 100px; }
  .role--concrete { left: 174px; }

  .divider {
    position: absolute; left: 145px; right: 0; top: 107px;
    height: 2px; background: var(--accent);
  }

  .contact { position: absolute; left: 0; top: 115px; width: 100%; list-style: none; }
  .contact li {
    position: relative; height: 20.5px;
    font-size: 13px; line-height: 20.5px;
  }
  .contact .label {
    position: absolute; right: calc(100% - 134px);
    font-family: "Libre Baskerville", Georgia, serif;
    font-style: italic; font-weight: 700;
    font-size: 10px; color: var(--label);
  }
  .contact .value { position: absolute; left: 145px; color: var(--ink); word-spacing: 3px; }
</style>
</head>
<body>
  <section class="card card--front" aria-label="Card front">
    <div class="front-wordmark">Kestrel Rehab</div>
  </section>

  <section class="card card--back" aria-label="Card back">
    <div class="back-brand">Kestrel Rehab</div>
    <div class="back-name">Daniel Whitcombe, Jr.</div>
    <div class="back-roles">
      <span class="role role--gc">General Contractor</span>
      <span class="role role--remodel">Home Remodel</span>
      <span class="role role--concrete">Concrete Alternatives</span>
    </div>
    <div class="divider"></div>
    <ul class="contact">
      <li><span class="label">t:</span><span class="value">555 014 2290</span></li>
      <li><span class="label">e:</span><span class="value">dwhitcombejr@example.com</span></li>
      <li><span class="label">w:</span><span class="value">www. kestrelrehab.com</span></li>
      <li><span class="label">i:</span><span class="value">Kestrel_Rehab</span></li>
    </ul>
  </section>
</body>
</html>
```